Design a label for horse salt

I need a label for the packaging for horse salt.

Label size is 99.1mm x 67.7mm

Information on the label includes:

Not for Human Consumption
SALT
Approx 530gms
Ingredients: 100% Additive Free Natural Solar Sea Salt
Packed in Queensland by Corvella Horse Feed

You may also include other interesting marketing or facts at your discretion (subject to approval)

I would like a background image included.

included is the logo for the Corvella Horse Feed.

```html
<!DOCTYPE html>
<html lang="en">
<head>
<meta charset="utf-8">
<title>Horse Salt Label</title>
<link rel="stylesheet" href="https://fonts.googleapis.com/css2?family=Montserrat:wght@400;500;600;700&family=Playfair+Display:wght@900&display=swap">
<style>
  :root {
    --backdrop: #a0e8b8;
    --label-black: #0c0c0c;
    --salt-brown: #a46c46;
    --copy-brown: #b9825c;
    --warning-red: #e3262c;
    --badge-orange: #f2952c;
    --white: #ffffff;
    --photo-dark: #7e4129;
    --photo-mid: #b35a2c;
    --photo-light: #c98757;
  }
  * { margin: 0; padding: 0; box-sizing: border-box; }
  html, body {
    width: 1200px; height: 749px; overflow: hidden;
    background: var(--backdrop);
    font-family: "Montserrat", Arial, sans-serif;
  }
  .label {
    position: absolute; left: 164px; top: 80px;
    width: 872px; height: 589px;
    background: var(--label-black);
    overflow: hidden;
    box-shadow: 0 2px 6px rgba(0,0,0,0.25);
  }
  .label-art { position: absolute; inset: 0; }
  .brand {
    position: absolute; left: 30px; top: 44px;
    display: flex; align-items: flex-start; gap: 8px;
    color: var(--white); font-size: 14px; font-weight: 500; line-height: 1.25;
  }
  .brand-dot {
    width: 12px; height: 12px; border-radius: 50%;
    background: var(--white); margin-top: 3px;
  }
  .copy {
    position: absolute; left: 5px; width: 480px;
    text-align: center;
  }
  .warning-top { top: 166px; color: var(--warning-red); font-size: 23px; font-weight: 400; }
  .warning-main { top: 205px; color: var(--warning-red); font-size: 23px; font-weight: 600; }
  .product-name {
    position: absolute; left: 40px; top: 222px;
    font-family: "Playfair Display", Georgia, serif;
    font-weight: 900; font-size: 162px; line-height: 1;
    color: var(--salt-brown); letter-spacing: 2px;
  }
  .weight-label { top: 416px; color: var(--white); font-size: 20px; font-weight: 500; }
  .weight-value { top: 444px; color: var(--white); font-size: 35px; font-weight: 700; }
  .packed {
    top: 510px; color: var(--copy-brown);
    font-size: 18.5px; font-weight: 400; line-height: 27px;
  }
  .badge-text { font-family: "Montserrat", Arial, sans-serif; font-weight: 500; }
</style>
</head>
<body>
  <div class="label">
    <svg class="label-art" width="872" height="589" viewBox="0 0 872 589">
      <defs>
        <linearGradient id="horsePhoto" x1="0" y1="0" x2="1" y2="1">
          <stop offset="0" stop-color="#c98757"/>
          <stop offset="0.5" stop-color="#b35a2c"/>
          <stop offset="1" stop-color="#7e4129"/>
        </linearGradient>
        <path id="badgeArc" d="M-77.8,13.7 A79,79 0 0 0 77.8,13.7" fill="none"/>
      </defs>
      <path d="M610,0 L872,0 L872,589 L520,589 C455,440 455,210 610,0 Z" fill="#7e4129"/>
      <path role="img" aria-label="Photograph of a chestnut horse's head with a white blaze"
            d="M640,0 L872,0 L872,589 L548,589 C490,440 492,220 640,0 Z" fill="url(#horsePhoto)"/>
      <g class="badge" transform="translate(556,133) scale(1.2)">
        <polygon fill="#0c0c0c" stroke="#ffffff" stroke-width="1.2"
          points="100,0 92.2,12.1 96.6,25.9 85.9,35.6 86.6,50 73.8,56.6 70.7,70.7 56.6,73.8 50,86.6 35.6,85.9 25.9,96.6 12.1,92.2 0,100 -12.1,92.2 -25.9,96.6 -35.6,85.9 -50,86.6 -56.6,73.8 -70.7,70.7 -73.8,56.6 -86.6,50 -85.9,35.6 -96.6,25.9 -92.2,12.1 -100,0 -92.2,-12.1 -96.6,-25.9 -85.9,-35.6 -86.6,-50 -73.8,-56.6 -70.7,-70.7 -56.6,-73.8 -50,-86.6 -35.6,-85.9 -25.9,-96.6 -12.1,-92.2 0,-100 12.1,-92.2 25.9,-96.6 35.6,-85.9 50,-86.6 56.6,-73.8 70.7,-70.7 73.8,-56.6 86.6,-50 85.9,-35.6 96.6,-25.9 92.2,-12.1"/>
        <circle r="92" fill="#0c0c0c"/>
        <path class="leaf-icon" d="M-7,-40 C-9,-52 1,-60 11,-62 C11,-50 5,-40 -7,-40 Z M-9,-36 L3,-52"
              fill="#ffffff" stroke="#ffffff" stroke-width="1.2"/>
        <text class="badge-text" x="0" y="8" text-anchor="middle" fill="#f2952c" font-size="40">100%</text>
        <text class="badge-text" x="0" y="27" text-anchor="middle" fill="#f2952c" font-size="16">Additive Free</text>
        <text class="badge-text" fill="#ffffff" font-size="13">
          <textPath href="#badgeArc" startOffset="50%" text-anchor="middle">Natural Solar Sea Salt</textPath>
        </text>
      </g>
    </svg>

    <div class="brand"><span class="brand-dot"></span><span>Corvella<br>Horse Feed</span></div>

    <p class="copy warning-top">Not for</p>
    <p class="copy warning-main">Human Consumption</p>
    <h1 class="product-name">SALT</h1>
    <p class="copy weight-label">Approx</p>
    <p class="copy weight-value">530gms</p>
    <p class="copy packed">Packed in Queensland Australia<br>by Corvella Horse Feed</p>
  </div>
</body>
</html>
```